TALLIS AT DWELLINGS, LLC Webpage portfolio

I want to create a Website that allows my potential clients to browse my Skilled work via before and after photos. I want the website to enhance the work that I provide and potentially drive new business, or at least solidify my work.
I also do 3D CAD and Modeling of New Spaces and it would be nice to show some of that work from pencil design to 3D modeling, which I feel may help give me more clients.

The website needs to show a solid carpenter/company with the skills to get any project completed.

Types of Jobs - Custom Carpentry & Finishes, Kitchens, Baths, Basements, Decks, Porches, Whole House Renovation - Skilled Craftsmanship (Hardwood Flooring, Floor and Wall Tile) and much more...

Target Market(s)

Residential Home Renovation, Kitchen and Bath Renovation, Home Improvement

Industry/Entity Type

Residential Construction

Number of Pages Required

5+ page

Font styles to use
Sans Serif
Script

Requirements
Must have
• Similar to Rimvale.com, except for Tallis At Dwellings.
• Must be inviting.
• My Services Offered
• A way to reach me or contact me for estimates with some sort of Screening Questionare.
Nice to have
• Inviting Colors
Should not have
• Not sure at this time

```html
<!DOCTYPE html>
<html lang="en">
<head>
<meta charset="utf-8">
<title>Tallis At Dwellings</title>
<link href="https://fonts.googleapis.com/css2?family=Montserrat:wght@400;600;700&family=Open+Sans:ital,wght@0,400;0,600;1,400&family=Oswald:wght@500&display=swap" rel="stylesheet">
<style>
:root{
  --blue:#2bb6f3;
  --yellow:#f8c22e;
  --navy:#1d2c3e;
  --dark:#2c2c2c;
  --darker:#242424;
  --text:#444;
  --muted:#777;
  --white:#fff;
}
*{margin:0;padding:0;box-sizing:border-box}
html,body{width:1200px;height:2584px;overflow:hidden;background:var(--white)}
body{position:relative;font-family:"Open Sans",sans-serif;color:var(--text)}
.abs{position:absolute}
h2{font-family:"Montserrat",sans-serif;font-weight:700;color:var(--navy);font-size:23px;letter-spacing:.5px}

/* header */
.topbar{left:0;top:0;width:1200px;height:124px;background:var(--blue)}
.brand-panel{left:0;top:0;width:500px;height:124px}
.brand{left:150px;top:40px;display:flex;align-items:center;gap:12px;font-family:"Montserrat",sans-serif;font-weight:700;font-size:27px;color:var(--navy)}
.brand-mark{width:20px;height:20px;background:var(--navy)}
.contact-item{color:var(--white);font-size:11px;line-height:19px;display:flex;gap:18px;align-items:center}
.social-bar{left:914px;top:107px;width:286px;height:34px;background:var(--yellow);display:flex;align-items:center;gap:22px;padding-left:26px}
.social-bar span{width:12px;height:12px;border-radius:50%;background:var(--navy)}
.nav{left:183px;top:166px;display:flex;gap:0;font-family:"Montserrat",sans-serif;font-size:11.5px;font-weight:600;color:var(--navy)}
.nav a{margin-right:57px;text-decoration:none;color:inherit;position:relative}
.nav a.active::after{content:"";position:absolute;left:0;right:0;top:21px;height:3px;background:var(--yellow)}

/* hero */
.hero{left:0;top:207px;width:1200px;height:479px;background:linear-gradient(180deg,#5a3a20 0%,#7b5530 45%,#4a3220 100%)}
.hero-title{left:0;top:365px;width:1200px;text-align:center;font-family:"Montserrat",sans-serif;font-weight:700;font-size:45px;color:var(--white);letter-spacing:1px}
.hero-sub{left:0;top:420px;width:1200px;text-align:center;font-family:"Montserrat",sans-serif;font-weight:600;font-size:26px;color:var(--white)}
.btn{display:flex;height:44px;font-family:"Montserrat",sans-serif;font-weight:600;font-size:12px;color:var(--navy)}
.btn .label{background:var(--yellow);display:flex;align-items:center;justify-content:center;clip-path:polygon(0 0,88% 0,100% 100%,0 100%)}
.btn .arrow{background:#333;margin-left:-18px;display:flex;align-items:center;justify-content:center}

/* services */
.services-title{left:153px;top:703px}
.lead{font-size:11.5px;line-height:22px;color:var(--text)}
.card{width:274px;height:162px}
.card .photo{height:112px;background:linear-gradient(135deg,#cfd3d6,#8e959b)}
.card .band{height:50px;background:var(--blue);color:var(--white);font-family:"Montserrat",sans-serif;font-weight:600;font-size:18px;padding:12px 14px;letter-spacing:.5px}

/* projects */
.projects{left:0;top:1295px;width:1200px;height:382px;background:linear-gradient(90deg,#3a3530,#55504a 50%,#3a3530)}
.projects h2{color:var(--white)}
.shot{width:443px}
.shot .photo{height:171px}
.shot .band{height:27px;background:var(--yellow);font-family:"Montserrat",sans-serif;font-weight:700;font-size:12px;color:var(--navy);padding:6px 10px}
.circle-arrow{width:36px;height:36px}

/* testimonial */
.quote-box{left:145px;top:1777px;width:895px;height:99px;border:2px solid var(--blue);padding:22px 24px 0 80px;font-style:italic;font-size:12.5px;line-height:23px;color:#666}
.avatar{left:155px;top:1898px;width:54px;height:52px;background:linear-gradient(#c9b6a3,#8a7a6a)}

/* footer */
.footer{left:0;top:2024px;width:1200px;height:560px;background:var(--dark)}
.foot-label{font-size:8.5px;color:#aaa;font-weight:600;letter-spacing:.5px}
.foot-value{font-size:11.5px;color:var(--white);font-weight:600;margin-top:4px}
.quote-form{left:462px;top:1960px;width:274px;height:367px;background:var(--yellow);padding:0 32px}
.quote-form h3{font-family:"Montserrat",sans-serif;font-weight:700;font-size:18px;color:var(--navy);text-align:center;margin:34px 0 26px}
.field{border-bottom:1px solid #5b4a1a;font-size:10px;color:#333;padding-bottom:2px;margin-bottom:20px}
.map{left:736px;top:2024px;width:464px;height:303px;background:linear-gradient(135deg,#e6e6e6,#cfcfcf 60%,#b9b9b9)}
.newsletter{left:141px;top:2410px;width:895px;height:83px;background:#3a3a3a}
.newsletter .title{position:absolute;left:32px;top:20px;font-family:"Oswald",sans-serif;font-weight:500;font-size:19px;line-height:22px;color:#ddd}
.copyright{left:141px;top:2551px;font-size:9px;color:#aaa}
.foot-social span{width:26px;height:26px;border:1px solid #555;border-radius:50%;display:inline-block;margin-right:11px}
</style>
</head>
<body>

<!-- header -->
<div class="abs topbar"></div>
<svg class="abs brand-panel" viewBox="0 0 500 124" aria-hidden="true"><polygon points="0,0 445,0 495,62 445,124 0,124" fill="#f4f8fb"/></svg>
<div class="abs brand"><span class="brand-mark"></span>Tallis At Dwellings</div>

<div class="abs contact-item" style="left:629px;top:27px">
  <svg width="16" height="16" viewBox="0 0 24 24"><path d="M6.6 10.8a15 15 0 0 0 6.6 6.6l2.2-2.2c.3-.3.7-.4 1-.2 1.1.4 2.3.6 3.6.6.6 0 1 .4 1 1V20c0 .6-.4 1-1 1A17 17 0 0 1 3 4c0-.6.4-1 1-1h3.5c.6 0 1 .4 1 1 0 1.3.2 2.5.6 3.6.1.3 0 .7-.2 1z" fill="#fff"/></svg>
  <div>1-555-38-912<br>info@tallisdwellings.com</div>
</div>
<div class="abs contact-item" style="left:853px;top:27px">
  <svg width="18" height="16" viewBox="0 0 24 20"><path d="M12 0 0 10h3v10h7v-6h4v6h7V10h3z" fill="#fff"/></svg>
  <div>Harbor Lane Road<br>Sydney, Australia</div>
</div>
<div class="abs social-bar"><span></span><span></span><span></span><span></span></div>

<nav class="abs nav">
  <a class="active">HOME</a><a>ABOUT</a><a>PROJECTS</a><a>SERVICES</a><a>TESTIMONIALS</a><a>GALLERY</a><a>GET A QUOTE</a><a>CONTACT</a>
</nav>

<!-- hero -->
<div class="abs hero" role="img" aria-label="Warm wooden kitchen interior with cabinets and countertop"></div>
<div class="abs hero-title">DESIGNING- CREATION- MAKING</div>
<div class="abs hero-sub">WE MAKE YOUR HOME BEAUTIFUL</div>
<div class="abs btn" style="left:447px;top:501px">
  <div class="label" style="width:210px">GET A QUOTE NOW</div>
  <div class="arrow" style="width:77px"><svg width="12" height="12" viewBox="0 0 12 12"><path d="M2 6h7M6 2l4 4-4 4" stroke="#fff" stroke-width="2" fill="none"/></svg></div>
</div>

<!-- services -->
<h2 class="abs services-title">OUR SERVICES</h2>
<p class="abs lead" style="left:153px;top:735px;width:880px">From &nbsp;Custom Carpentry &amp; Finishes, Kitchens, Baths, Basements, Decks, Porches, Whole House Renovation - Skilled Craftsmanship (Hardwood Flooring, Floor and Wall Tile) and much more...</p>

<div class="abs card" style="left:147px;top:810px"><div class="photo" role="img" aria-label="Worker renovating a wall"></div><div class="band">RENOVATION</div></div>
<div class="abs card" style="left:460px;top:810px"><div class="photo" role="img" aria-label="Plumber in a kitchen"></div><div class="band">PLUMBING</div></div>
<div class="abs card" style="left:774px;top:810px"><div class="photo" role="img" aria-label="Brush painting a surface" style="background:linear-gradient(135deg,#9fb7cf,#3d5d8a)"></div><div class="band">PAINTING</div></div>
<div class="abs card" style="left:147px;top:1007px"><div class="photo" role="img" aria-label="Electrician fixing a socket"></div><div class="band">ELECTRICAL</div></div>
<div class="abs card" style="left:460px;top:1007px"><div class="photo" role="img" aria-label="Drilling into a wall panel" style="background:linear-gradient(135deg,#e8e3df,#b56a4e)"></div><div class="band">WALLS</div></div>
<div class="abs card" style="left:774px;top:1007px"><div class="photo" role="img" aria-label="Red roof tiles being laid" style="background:linear-gradient(135deg,#d36a4a,#9c3a24)"></div><div class="band">ROOFING</div></div>

<div class="abs btn" style="left:497px;top:1210px;height:38px">
  <div class="label" style="width:160px">MORE JOBS</div>
  <div class="arrow" style="width:52px"><svg width="12" height="12" viewBox="0 0 12 12"><path d="M2 6h7M6 2l4 4-4 4" stroke="#fff" stroke-width="2" fill="none"/></svg></div>
</div>

<!-- projects -->
<div class="abs projects" role="img" aria-label="Dimmed background of workers on site"></div>
<h2 class="abs" style="left:153px;top:1326px;color:#fff">OUR PROJECTS</h2>
<p class="abs lead" style="left:153px;top:1356px;color:#eee;font-size:11px">Please check all kind of works we done in recent past and check the before after so you can have idea about our expertize and quality of work.</p>
<div class="abs shot" style="left:141px;top:1419px"><div class="photo" role="img" aria-label="Kitchen before renovation" style="background:linear-gradient(135deg,#8a8a6e,#5d6a5c)"></div><div class="band">BEFORE</div></div>
<div class="abs shot" style="left:602px;top:1419px"><div class="photo" role="img" aria-label="Kitchen after renovation" style="background:linear-gradient(135deg,#a97b52,#4a3322)"></div><div class="band">AFTER</div></div>
<svg class="abs circle-arrow" style="left:60px;top:1494px" viewBox="0 0 36 36"><circle cx="18" cy="18" r="16" stroke="#fff" stroke-width="2" fill="none"/><path d="M21 11l-7 7 7 7" stroke="#fff" stroke-width="2" fill="none"/></svg>
<svg class="abs circle-arrow" style="left:1090px;top:1494px" viewBox="0 0 36 36"><circle cx="18" cy="18" r="16" stroke="#fff" stroke-width="2" fill="none"/><path d="M15 11l7 7-7 7" stroke="#fff" stroke-width="2" fill="none"/></svg>

<!-- testimonial -->
<h2 class="abs" style="left:153px;top:1694px">CLIENTS TESTIMONIAL</h2>
<p class="abs lead" style="left:153px;top:1725px;font-size:11px">Check all our client's say about our work, quality and dedication.</p>
<div class="abs quote-box">Technician came over to do a few odd jobs and did great work. Fixed a window, a sink and an electrical plug all for a reasonable price. I satisfy with his work and your service. Would definitely use them again.</div>
<svg class="abs" style="left:178px;top:1798px" width="32" height="24" viewBox="0 0 32 24"><path d="M0 24V12C0 5 4 1 12 0v5c-4 1-5 3-5 7h5v12zM18 24V12c0-7 4-11 12-12v5c-4 1-5 3-5 7h5v12z" fill="var(--yellow)"/></svg>
<div class="abs avatar" role="img" aria-label="Client portrait"></div>
<div class="abs" style="left:224px;top:1902px;font-family:Montserrat,sans-serif;font-weight:600;font-size:13px;color:var(--navy)">Marla Quist</div>
<div class="abs" style="left:224px;top:1922px;font-size:10.5px;color:#999">CEO Of Brightmoor</div>
<svg class="abs" style="left:938px;top:1917px" width="78" height="4"><rect width="22" height="3" fill="var(--yellow)"/><rect x="26" width="22" height="3" fill="#ddd"/><rect x="52" width="22" height="3" fill="#ddd"/></svg>

<!-- footer -->
<div class="abs footer"></div>
<div class="abs" style="left:145px;top:2081px;width:18px;height:1px;background:var(--yellow)"></div>
<div class="abs" style="left:172px;top:2073px;font-family:Montserrat,sans-serif;font-weight:600;font-size:13px;color:var(--yellow)">AUSTRALIA</div>

<svg class="abs" style="left:142px;top:2118px" width="12" height="16" viewBox="0 0 12 16"><path d="M6 0a6 6 0 0 0-6 6c0 4.5 6 10 6 10s6-5.5 6-10a6 6 0 0 0-6-6zm0 8.5A2.5 2.5 0 1 1 6 3.5a2.5 2.5 0 0 1 0 5z" fill="#999"/></svg>
<div class="abs" style="left:168px;top:2117px"><div class="foot-label">FIND US</div><div class="foot-value">48th, Elm Terrace, LONDON</div></div>
<svg class="abs" style="left:144px;top:2172px" width="9" height="16" viewBox="0 0 9 16"><rect x=".5" y=".5" width="8" height="15" rx="1.5" stroke="#999" fill="none"/><rect x="3" y="12.5" width="3" height="1" fill="#999"/></svg>
<div class="abs" style="left:168px;top:2172px"><div class="foot-label">CALL US TODAY</div><div class="foot-value">+00 912 438 7650</div></div>
<svg class="abs" style="left:141px;top:2229px" width="14" height="11" viewBox="0 0 14 11"><rect width="14" height="11" fill="#999"/><path d="M0 0l7 6 7-6" stroke="#2c2c2c" fill="none"/></svg>
<div class="abs" style="left:168px;top:2227px"><div class="foot-label">EMAIL US NOW</div><div class="foot-value">contact@tallisdwellings.com</div></div>
<svg class="abs" style="left:141px;top:2315px" width="50" height="12" viewBox="0 0 50 12"><path d="M6 1l5 5-5 5-5-5z" fill="#777"/><path d="M25 1l5 5-5 5-5-5z" fill="var(--yellow)"/><path d="M44 1l5 5-5 5-5-5z" fill="#777"/></svg>

<div class="abs map" role="img" aria-label="Street map of the office area"></div>

<form class="abs quote-form">
  <h3>REQUEST A QUOTE</h3>
  <div class="field">Name</div>
  <div class="field">Email</div>
  <div class="field">Phone</div>
  <div class="field" style="height:68px">Message</div>
  <div class="btn" style="height:36px;margin:34px 0 0 44px">
    <div class="label" style="width:112px;background:#fff;font-size:10px">SUBMIT</div>
    <div class="arrow" style="width:36px"><svg width="10" height="10" viewBox="0 0 12 12"><path d="M2 6h7M6 2l4 4-4 4" stroke="#fff" stroke-width="2" fill="none"/></svg></div>
  </div>
</form>

<div class="abs newsletter">
  <div class="title">LIKE OUR WORK?<br>RECEIVE OUR EMAIL NEWSLETTER</div>
  <div style="position:absolute;left:368px;top:25px;width:346px;height:36px;background:#8a8a8a;font-size:10px;color:#eee;padding:11px 10px">Your email ID</div>
  <div class="btn" style="position:absolute;left:718px;top:25px;height:36px">
    <div class="label" style="width:124px;font-size:9.5px">SUBSCRIBE</div>
  </div>
</div>

<div class="abs copyright">© 2017, ALL RIGHTS RESERVED. <span style="color:#fff">TALLISDWELLINGS.COM</span></div>
<div class="abs foot-social" style="left:855px;top:2543px"><span></span><span></span><span></span><span></span><span></span></div>

</body>
</html>
```